Business card for Eyelash extension salon in Beverly Hills,California USA

We need new business card for our salon in Beverly Hills. The salon name is 'Lumarra' . We would like to have...Business name: Lumarra Name of person: will provide later Address 6128 N.Corbel Ridge Blvd Beverly Hills , CA 90210 Phone: will provide later (Text only) Web: www.lumarrastudio-example.com Pictogrid icon, Friendvale icon follow us for seasonal campaign and news @lumarrastudioexample Design should look elegant, high-end, clean, simple, cohesive with my brand. Please refer my brand board. Business name color will be metallic bronzy color. Im thinking grey background or white background. Thanks

Target Market(s)

25-35. Gender neutral. People who are in Entertainment business industry.
This is High-end Eyelash extension salon in Beverly Hills

Industry/Entity Type

Beauty Salon

Contact Information for Business Card

Business name: Lumarra
Name of person: will provide later
Address 6128 N.Corbel Ridge Blvd Beverly Hills , CA 90210
Phone: will provide later (Text only)
Web: www.lumarrastudio-example.com
Pictogrid icon, Friendvale icon
follow us for seasonal campaign and news @lumarrastudioexample

Requirements
Must have
• Beautiful, elegant, clean and simple look but very attractive and modern
Should not have
• We don't like too clutter, too busy designs.

```html
<!DOCTYPE html>
<html lang="en">
<head>
<meta charset="utf-8">
<title>Lumarra Beverly Hills – Business Card</title>
<link href="https://fonts.googleapis.com/css2?family=Libre+Baskerville:wght@400;700&family=Playfair+Display:wght@700&family=Josefin+Sans:wght@400&display=swap" rel="stylesheet">
<style>
  :root {
    --bronze: #87674f;
    --sand: #c8ab8c;
    --icon-sand: #c9a987;
    --ink: #1b1b1b;
    --paper: #ffffff;
    --canvas: #ffffff;
  }
  * { margin: 0; padding: 0; box-sizing: border-box; }
  html, body { width: 1200px; height: 900px; overflow: hidden; background: var(--canvas); }
  .canvas { position: relative; width: 1200px; height: 900px; }

  .card {
    position: absolute;
    width: 684px;
    height: 380px;
    box-shadow: 0 6px 16px rgba(0,0,0,0.35);
    overflow: hidden;
  }
  .card--front { left: 66px; top: 38px; background: var(--paper); }
  .card--back { left: 399px; top: 468px; background: var(--bronze); }

  .holder-name {
    position: absolute; left: 39px; top: 38px;
    font-family: "Playfair Display", serif; font-weight: 700;
    font-size: 44px; letter-spacing: 2px; color: var(--bronze);
  }

  .contact {
    position: absolute; left: 48px;
    display: flex; align-items: center; gap: 16px;
    font-family: "Libre Baskerville", serif; font-size: 19px; color: var(--ink);
  }
  .contact svg { width: 28px; height: 28px; flex: none; }
  .contact--phone { top: 123px; }
  .contact--web { top: 186px; }
  .contact--address { top: 256px; }

  .wordmark {
    position: absolute; text-align: right;
    font-family: "Libre Baskerville", serif; font-weight: 400;
  }
  .wordmark__name { display: block; line-height: 1; }
  .wordmark__place {
    display: block; font-family: "Josefin Sans", sans-serif; letter-spacing: 2px;
  }
  .card--front .wordmark { right: 70px; top: 92px; color: var(--bronze); }
  .card--front .wordmark__name { font-size: 58px; }
  .card--front .wordmark__place { font-size: 11px; margin-top: 14px; padding-right: 4px; }
  .card--back .wordmark { left: 0; right: 0; top: 110px; text-align: center; color: var(--paper); }
  .card--back .wordmark__name { font-size: 112px; }
  .card--back .wordmark__place { font-size: 18px; letter-spacing: 3px; margin-top: 26px; padding-left: 210px; }

  .footer-band { position: absolute; left: 0; bottom: 0; width: 684px; height: 70px; }
  .social {
    position: absolute; right: 35px; bottom: 24px;
    display: flex; align-items: center; gap: 6px;
    font-family: "Libre Baskerville", serif; font-size: 17px; color: var(--ink);
  }
  .social__mark { width: 19px; height: 19px; background: var(--bronze); border-radius: 3px; }
  .social__handle { margin-left: 4px; }
</style>
</head>
<body>
<main class="canvas">

  <section class="card card--front" aria-label="Business card front">
    <h1 class="holder-name">NAME</h1>

    <p class="contact contact--phone">
      <svg viewBox="0 0 28 28" aria-hidden="true">
        <path d="M3 10c0-3 5-5 11-5s11 2 11 5v2h-6v-2c-2-1-8-1-10 0v2H3z" fill="var(--icon-sand)"/>
        <path d="M8 13h12l3 10H5z" fill="var(--icon-sand)"/>
        <circle cx="14" cy="18" r="3" fill="var(--paper)"/>
      </svg>
      123 456 789
    </p>

    <p class="contact contact--web">
      <svg viewBox="0 0 28 28" aria-hidden="true">
        <rect x="2" y="7" width="24" height="15" fill="var(--icon-sand)"/>
        <path d="M2 7l12 9 12-9" fill="none" stroke="var(--paper)" stroke-width="1.6"/>
      </svg>
      www.lumarrastudio-example.com
    </p>

    <p class="contact contact--address">
      <svg viewBox="0 0 28 28" aria-hidden="true">
        <path d="M14 1a9 9 0 0 0-9 9c0 7 9 17 9 17s9-10 9-17a9 9 0 0 0-9-9z" fill="var(--icon-sand)"/>
        <circle cx="14" cy="10" r="3.4" fill="var(--paper)"/>
      </svg>
      6128 N.Corbel Ridge Blvd Beverly Hills , CA 90210
    </p>

    <div class="wordmark">
      <span class="wordmark__name">Lumarra</span>
      <span class="wordmark__place">BEVERLY HILLS</span>
    </div>

    <svg class="footer-band" viewBox="0 0 684 70" aria-hidden="true">
      <rect width="684" height="70" fill="var(--bronze)"/>
      <polygon points="341,0 684,0 684,70 379,70" fill="var(--sand)"/>
    </svg>

    <p class="social">
      <span class="social__mark" aria-label="Friendvale"></span>
      <span class="social__mark" aria-label="Pictogrid"></span>
      <span class="social__handle">@lumarrastudioexample</span>
    </p>
  </section>

  <section class="card card--back" aria-label="Business card back">
    <div class="wordmark">
      <span class="wordmark__name">Lumarra</span>
      <span class="wordmark__place">BEVERLY HILLS</span>
    </div>
  </section>

</main>
</body>
</html>
```